Creat new BusinessCard for Brightfold Consulting!

Hello Creativ Designer. I need a new Businesscard for our brand new Company "Brightfold Training". We do Consulting for a better Life & Work Situation. to create Fulfillment, Sense, Motivation and healthy Work Places in Company's. So we try to create a better World and help the employee to like what they do!
So we would like to have 2 Sites on the card. On the Back we want to put this words: "The sole meaning of life, is to serve humanity" (it can be vertical oder horizontal). In the front there is the Logo (Black or White) and Adress+ and Slogan.

Slogan on the front: -Make your Business & Life to a better place-

Name: Lukas Verhoff
Titel: Founder - Visionary - Trainer
Adress: Based in Switzerland

Tel: +41 (0) 71 583 42 17
Email: hello@brightfold-training.ch
Homepage: www.brightfold-training.ch

Thanks for your inspired Ideas and your help to make the world to a better place! IT has to be ready to print and normal Size.

Target Market(s)

insurance, Bank, Telecom, industry, IT, Medical

Contact Information for Business Card

Breite: 85 mm x Höhe: 55 mm

Colors

Designer to choose colors to be used in the design.

Requirements
Nice to have
• Thanks for your Ideas so far!
• Maybe you can try/play with the colors: Purple Code #652C8F and Grey #979797 from the Zelvor Logo purple and grey (but only a soft combination, not to much)

```html
<!DOCTYPE html>
<html lang="en">
<head>
<meta charset="utf-8">
<title>Brightfold Training – Business Card</title>
<link href="https://fonts.googleapis.com/css2?family=Roboto:ital,wght@0,400;0,500;0,700;1,400;1,500&family=Roboto+Condensed:wght@400;500&display=swap" rel="stylesheet">
<style>
  :root {
    --page-bg: #e9e6e2;
    --card-dark: #000000;
    --card-light: #f1f1f1;
    --ink-light: #ffffff;
    --ink-dark: #111111;
    --ink-muted: #555555;
    --rule: #6a6a6a;
  }
  html, body {
    margin: 0;
    padding: 0;
    width: 1200px;
    height: 960px;
    overflow: hidden;
    background: var(--page-bg);
  }
  .canvas {
    position: relative;
    width: 1200px;
    height: 960px;
  }
  .card {
    position: absolute;
    width: 600px;
    height: 343px;
    border-radius: 22px;
    box-sizing: border-box;
    text-align: center;
  }
  .card--front {
    left: 314px;
    top: 113px;
    background: var(--card-dark);
    color: var(--ink-light);
    font-family: "Roboto", sans-serif;
  }
  .card--back {
    left: 311px;
    top: 472px;
    background: var(--card-light);
    color: var(--ink-dark);
    font-family: "Roboto", sans-serif;
  }
  .brand {
    position: absolute;
    left: 0;
    right: 0;
    display: flex;
    align-items: center;
    justify-content: center;
    gap: 14px;
  }
  .brand__dot {
    border-radius: 50%;
    flex: none;
  }
  .brand__name {
    font-weight: 700;
    letter-spacing: 1px;
    text-transform: uppercase;
    white-space: nowrap;
  }
  .card--front .brand { top: 100px; }
  .card--front .brand__dot { width: 44px; height: 44px; background: var(--ink-light); }
  .card--front .brand__name { font-size: 24px; color: var(--ink-light); }
  .front__rule {
    position: absolute;
    left: 116px;
    top: 182px;
    width: 370px;
    height: 1px;
    background: linear-gradient(to right, transparent, var(--rule) 20%, var(--rule) 80%, transparent);
  }
  .front__name {
    position: absolute;
    left: 0; right: 0;
    top: 204px;
    margin: 0;
    font-family: "Roboto Condensed", sans-serif;
    font-weight: 500;
    font-size: 22px;
    letter-spacing: 0.3px;
  }
  .front__title {
    position: absolute;
    left: 0; right: 0;
    top: 236px;
    margin: 0;
    font-family: "Roboto Condensed", sans-serif;
    font-size: 14.5px;
  }
  .front__contact {
    position: absolute;
    left: 0; right: 0;
    top: 262px;
    margin: 0;
    font-size: 14px;
    line-height: 19px;
  }
  .front__contact strong { font-weight: 500; }
  .front__slogan {
    position: absolute;
    left: 0; right: 0;
    top: 304px;
    margin: 0;
    font-size: 14px;
    font-style: italic;
    font-weight: 500;
  }
  .card--back .brand { top: 70px; flex-direction: column; gap: 18px; }
  .card--back .brand__dot { width: 100px; height: 100px; background: var(--ink-dark); }
  .card--back .brand__name { font-size: 28px; color: var(--ink-dark); }
  .back__quote {
    position: absolute;
    left: 0; right: 0;
    top: 297px;
    margin: 0;
    font-size: 14px;
    font-style: italic;
    font-weight: 500;
    color: var(--ink-muted);
  }
</style>
</head>
<body>
<main class="canvas">
  <section class="card card--front" aria-label="Business card front">
    <div class="brand">
      <span class="brand__dot"></span>
      <span class="brand__name">Brightfold Training</span>
    </div>
    <div class="front__rule"></div>
    <h1 class="front__name">LUKAS VERHOFF</h1>
    <p class="front__title">FOUNDER - VISIONARY - TRAINER</p>
    <p class="front__contact"><strong>PHONE</strong> : +41 (0) 71 583 42 17 | hello@brightfold-training.ch<br>www.brightfold-training.ch</p>
    <p class="front__slogan">Make your Business &amp; Life to a better place</p>
  </section>

  <section class="card card--back" aria-label="Business card back">
    <div class="brand">
      <span class="brand__dot"></span>
      <span class="brand__name">Brightfold Training</span>
    </div>
    <p class="back__quote">The sole meaning of life, is to serve humanity</p>
  </section>
</main>
</body>
</html>
```